Business Card Design

Divorce
Collaborative Family Law
Family Dispute Resolution
Family Law Property & Children

Target Market(s)

Australia

Industry/Entity Type

Business

Contact Information for Business Card

Delia Frampton
M App Law (Family Law) LLB (Hons) BA (Hons) Ass Dip Ag (HH)
Family Dispute Resolution Provider
Frampton Family Law
PO Box 4372 Wendlebury 3914
Phone 03 57218300 Fax 03 57218399 Email framptonfamilylaw@quillmail.example

Colors
f04a51

Requirements
Should not have
• Any reference to
United States or US terminology
the word Company

```html
<!DOCTYPE html>
<html lang="en">
<head>
<meta charset="utf-8">
<title>Frampton Family Law – Business Card</title>
<link rel="stylesheet" href="https://fonts.googleapis.com/css2?family=Lato:wght@400;700&display=swap">
<style>
  :root {
    --backdrop: #e8e8e8;
    --card-white: #fbfbfb;
    --brand-blue: #1a66b3;
    --brand-red: #f04a51;
    --band-text: #ffffff;
    --card-shadow: rgba(0, 0, 0, 0.14);
  }
  * { box-sizing: border-box; margin: 0; padding: 0; }
  html, body {
    width: 1200px;
    height: 864px;
    overflow: hidden;
    background: var(--backdrop);
    font-family: "Lato", sans-serif;
  }
  .canvas {
    position: relative;
    width: 1200px;
    height: 864px;
  }
  .business-card {
    position: absolute;
    left: 150px;
    top: 157px;
    width: 900px;
    height: 550px;
    background: var(--card-white);
    box-shadow: 0 14px 40px var(--card-shadow);
    overflow: hidden;
  }
  .identity {
    position: absolute;
    left: 148px;
    top: 104px;
    color: var(--brand-blue);
  }
  .identity__name {
    font-weight: 700;
    font-size: 34px;
    letter-spacing: 0.5px;
    text-transform: uppercase;
    line-height: 1;
  }
  .identity__phone {
    margin-top: 12px;
    font-size: 22px;
    letter-spacing: 0.8px;
    line-height: 1.2;
  }
  .identity__role {
    margin-top: 14px;
    font-size: 16px;
    font-weight: 700;
    letter-spacing: 0.4px;
    line-height: 1.3;
  }
  .identity__quals {
    margin-top: 4px;
    font-size: 14px;
    letter-spacing: 0.3px;
    line-height: 1.3;
  }
  .firm-mark {
    position: absolute;
    right: 92px;
    top: 118px;
    display: flex;
    align-items: center;
    gap: 12px;
    color: var(--brand-blue);
    font-weight: 700;
    font-size: 24px;
    letter-spacing: 0.4px;
  }
  .firm-mark__dot {
    width: 22px;
    height: 22px;
    border-radius: 50%;
    background: var(--brand-red);
  }
  .contact-band {
    position: absolute;
    left: 0;
    bottom: 0;
    width: 100%;
    height: 232px;
    background: var(--brand-blue);
    color: var(--band-text);
    padding: 44px 0 0 118px;
  }
  .contact-row {
    display: flex;
    align-items: flex-start;
    font-size: 21px;
    letter-spacing: 1px;
    line-height: 1.3;
  }
  .contact-row + .contact-row { margin-top: 14px; }
  .contact-row__icon {
    width: 24px;
    height: 24px;
    margin: 2px 20px 0 0;
    flex: none;
    fill: var(--band-text);
  }
  .contact-row__address { font-style: normal; }
</style>
</head>
<body>
<main class="canvas">
  <section class="business-card" aria-label="Business card for Delia Frampton">
    <div class="identity">
      <h1 class="identity__name">Delia Frampton</h1>
      <p class="identity__phone">03 57218300</p>
      <p class="identity__role">Family Dispute Resolution Provider</p>
      <p class="identity__quals">M App Law (Family Law) LLB (Hons) BA (Hons) Ass Dip Ag (HH)</p>
    </div>

    <div class="firm-mark">
      <span class="firm-mark__dot" aria-hidden="true"></span>
      <span class="firm-mark__name">Frampton Family Law</span>
    </div>

    <div class="contact-band">
      <div class="contact-row">
        <svg class="contact-row__icon" viewBox="0 0 24 24" aria-hidden="true">
          <path d="M12 3 1 12.5h3V21h6v-6h4v6h6v-8.5h3z"/>
        </svg>
        <address class="contact-row__address">
          Frampton Family Law<br>PO Box 4372 Wendlebury 3914
        </address>
      </div>
      <div class="contact-row">
        <svg class="contact-row__icon" viewBox="0 0 24 24" aria-hidden="true">
          <path d="M2 5h20v14H2z M3.5 6.5 12 13l8.5-6.5" fill="none" stroke="#fff" stroke-width="2"/>
        </svg>
        <span class="contact-row__text">framptonfamilylaw@quillmail.example</span>
      </div>
      <div class="contact-row">
        <svg class="contact-row__icon" viewBox="0 0 24 24" aria-hidden="true">
          <path d="M6 2h12v6H6z M2 9h20v9h-4v-4H6v4H2z M7 15h10v7H7z"/>
        </svg>
        <span class="contact-row__text">03 57218399</span>
      </div>
    </div>
  </section>
</main>
</body>
</html>
```